Design wireframe of E-commerce website *

We are a European online shoe store located in Sweden. The project is to redesign the first page of our e-commerce website https://kelvaro.se/skor
We want to receive creative ideas of what our website could look like while keeping all the functions and flows. The new design should be simple, lean and modern.
Specifications:
We have several guidelines for what we are expecting
- Redesign the frontend of our website first page https://kelvaro.se/skor and the child page https://www.kelvaro.se/skor/dam
- You need to provide a complete clickable wireframe of the target pages.
- All existing components should be in the new design.
- The pages should include all sections: header, footer, product lists and widgets. The page structure of the site should look as the example: https://www.trimsel.co.uk/shoes
- The design must be responsive and Mobile First which can be read from all browsers and different devices.
- You need to have in mind that we really want it to be mobile first, meaning
the mobile view is the most important one
- The new design should reflect our brands essence and come along with the new brandprofiles (fonts, icons...). For example http://brandprofile.trimsel.com/, but keep the logo and colour of the existing Kelvaro theme.
- The design should be user friendly.
- The design should be simple enough that the pages can be downloaded fast.
- The new design should look fashionable and be able to generating attracting
traffic.
- The text on the child page https://www.kelvaro.se/skor/dam should be handled in a better way and make it easier for users to know which page they are looking at. You can see the example at https://www.trimsel.co.uk/shoes/women but we are open to your good ideas as well.
- We do not want shelves in the design. Trimsel has it, but Kelvaro
should not.
- We want to keep the existing responsive sizes for product list which means 2, 4 or 6 pairs of shoes per row.
Practical Information:
We are located in Sweden and have working hours between 9:00 -12:00 (CEST)
Monday - Friday. We have limited capacity to answer every question you have
but will try to get back to you in our working hours as much as we can then
hopefully this can help you get a better understanding of what we are
looking for.
Future Possibilities:We are going to redesign the whole site
of https://www.kelvaro.se/skor so the winner
will have the chance to do all the pages in the near future. We are
actively seeking designers for future collaborations on a long-term basis
and it is possible to create a partnership if your work is impressive
enough. *

```html
<!DOCTYPE html>
<html lang="en">
<head>
<meta charset="utf-8">
<title>Kelvaro – Skor</title>
<link rel="stylesheet" href="https://fonts.googleapis.com/css2?family=Montserrat:wght@400;600;700;800&display=swap">
<style>
:root{
  --stage:#a9abad;
  --page:#ffffff;
  --ink:#1b1b1b;
  --muted:#8a8a8a;
  --line:#e2e2e2;
  --soft:#f2f2f2;
  --band:#eceeea;
  --green:#3aa84a;
  --sale:#e0393e;
  --hero-a:#ededed;
  --hero-b:#cfcfcf;
}
*{box-sizing:border-box;margin:0;padding:0}
html,body{width:1200px;height:2916px;overflow:hidden}
body{background:var(--stage);font-family:'Montserrat',sans-serif;color:var(--ink);position:relative}
.view{position:absolute;background:var(--page);display:flex;flex-direction:column;overflow:hidden}
.desktop{left:48px;top:48px;width:736px;height:2624px}
.tablet{left:800px;top:48px;width:152px;height:2520px}
.mobile{left:1008px;top:48px;width:152px;height:2752px}

/* header */
.site-header{display:flex;align-items:center;gap:14px;padding:0 18px;height:52px;border-bottom:1px solid var(--line);flex:0 0 auto}
.logo{font-weight:800;font-size:18px;letter-spacing:.5px}
.search{flex:0 0 150px;height:20px;border:1px solid var(--line);font-size:7px;color:var(--muted);display:flex;align-items:center;padding-left:6px;position:relative}
.search::after{content:"";position:absolute;right:0;top:0;width:20px;height:18px;background:var(--ink)}
.main-nav{display:flex;gap:14px;font-size:8px;font-weight:600;margin-left:10px}
.header-icons{margin-left:auto;display:flex;gap:10px}
.icon{width:12px;height:12px}

/* hero */
.hero{position:relative;height:352px;flex:0 0 auto;background:linear-gradient(135deg,var(--hero-a),var(--hero-b))}
.hero-copy{position:absolute;left:345px;top:120px;text-align:center}
.hero-copy .off{font-size:40px;font-weight:800;line-height:1}
.hero-copy .kind{font-size:34px;font-weight:800;line-height:1.05}
.btn{display:inline-block;background:var(--green);color:#fff;font-weight:700;font-size:10px;padding:8px 18px;margin-top:10px;text-transform:uppercase}
.arrow{position:absolute;top:160px;width:16px;height:22px;background:#333;display:flex;align-items:center;justify-content:center}
.arrow.left{left:0}.arrow.right{right:0}

/* categories */
.categories{display:grid;grid-template-columns:repeat(4,1fr);gap:4px;margin-top:12px;height:116px;flex:0 0 auto}
.cat{position:relative;background:linear-gradient(160deg,#c9c4bd,#8c847b)}
.cat:nth-child(2){background:linear-gradient(160deg,#d8d4cf,#6d6660)}
.cat:nth-child(3){background:linear-gradient(160deg,#b54a3c,#4a3a36)}
.cat:nth-child(4){background:linear-gradient(160deg,#a8b58c,#5a6848)}
.cat span{position:absolute;left:6px;bottom:6px;color:#fff;font-size:8px;font-weight:700;background:rgba(0,0,0,.45);padding:2px 5px}

/* products */
.products{display:grid;grid-template-columns:repeat(6,1fr);margin-top:20px;flex:0 0 auto}
.product{height:200px;padding:14px 10px 0;text-align:center;font-size:7px;line-height:1.5}
.products .product:nth-child(n+13):nth-child(-n+18),
.products .product:nth-child(n+25):nth-child(-n+30){background:var(--soft)}
.shot{height:92px;margin-bottom:10px;border-radius:2px}
.product b{display:block;font-size:10px;font-weight:800;letter-spacing:.3px}
.product span{display:block;color:var(--muted);white-space:nowrap;overflow:hidden;text-overflow:ellipsis}
.product em{font-style:normal;font-weight:700;font-size:9px}
.product em.sale{color:var(--sale)}
.c1{background:linear-gradient(180deg,#fff,#2e3340 60%,#fff)}
.c2{background:linear-gradient(180deg,#fff,#b9bdc4 60%,#fff)}
.c3{background:linear-gradient(180deg,#fff,#6b4a34 60%,#fff)}
.c4{background:linear-gradient(180deg,#fff,#1d1d1d 60%,#fff)}
.c5{background:linear-gradient(180deg,#fff,#7d8a5a 60%,#fff)}
.c6{background:linear-gradient(180deg,#fff,#c7a7b6 60%,#fff)}
.more{display:block;margin:12px auto 24px;width:110px;height:18px;background:#cfcfcf;color:#fff;font-size:7px;font-weight:600;text-align:center;line-height:18px;flex:0 0 auto}

/* usp cards */
.usps{display:grid;grid-template-columns:1fr 1fr;gap:22px 26px;padding:40px 90px;background:var(--soft);height:420px;flex:0 0 auto}
.usp{background:#fff;border:1px solid var(--line);text-align:center;padding:30px 30px 0;font-size:8px;line-height:1.5}
.usp .btn{font-size:6px;padding:4px 12px}

/* promise band */
.promise{background:var(--band);text-align:center;padding:38px 0;height:130px;font-size:8px;line-height:1.6;flex:0 0 auto}
.promise strong{display:block;color:var(--green);font-size:12px;font-weight:700}

/* footer */
.site-footer{flex:1;padding:26px 40px 0;font-size:7px;line-height:1.8}
.foot-cols{display:grid;grid-template-columns:repeat(4,1fr) 1.4fr;gap:16px}
.foot-cols h4{font-size:8px;font-weight:700;margin-bottom:4px}
.news{display:flex;margin-top:4px}
.news i{flex:1;border:1px solid var(--line);height:16px}
.news b{background:var(--ink);color:#fff;padding:0 8px;line-height:16px}
.foot-base{display:flex;align-items:center;gap:120px;margin-top:50px;border-top:1px solid var(--line);padding-top:20px}
.foot-base .logo{font-size:22px}
.pay{font-weight:800;font-size:12px}
.foot-base small{margin-left:auto;color:var(--muted)}

/* narrow views */
.narrow .site-header{height:30px;padding:0 8px;gap:6px}
.narrow .logo{font-size:11px}
.narrow .icon{width:8px;height:8px}
.narrow .header-icons{gap:5px}
.narrow .hero{height:110px}
.narrow .hero-copy{left:58px;top:20px}
.narrow .hero-copy .off{font-size:16px}
.narrow .hero-copy .kind{font-size:13px}
.narrow .btn{font-size:5px;padding:3px 7px;margin-top:4px}
.narrow .arrow{display:none}
.narrow .categories{grid-template-columns:1fr 1fr;height:200px;margin-top:4px}
.narrow .cat span{font-size:5px}
.narrow .products{grid-template-columns:1fr 1fr;margin-top:10px;padding:0 4px}
.narrow .product{height:120px;padding:6px 4px 0;font-size:5px;line-height:1.4}
.narrow .products .product{background:none}
.narrow .shot{height:62px;margin-bottom:5px}
.narrow .product b{font-size:6px}
.narrow .product em{font-size:6px}
.narrow .more{width:80px;height:14px;line-height:14px;font-size:5px;margin:10px auto 22px}
.narrow .usps{grid-template-columns:1fr;padding:14px 12px;gap:12px;height:auto}
.narrow .usp{height:98px;padding:16px 10px 0;font-size:6px}
.narrow .usp .btn{font-size:5px;padding:3px 8px}
.narrow .promise{height:90px;padding:18px 6px;font-size:5px}
.narrow .promise strong{font-size:7px}
.narrow .site-footer{padding:14px 10px 0;font-size:5px}
.narrow .foot-cols{grid-template-columns:1fr;gap:10px}
.narrow .foot-cols h4{font-size:6px}
.narrow .foot-base{flex-direction:column;align-items:flex-start;gap:10px;margin-top:18px;padding-top:12px}
.narrow .foot-base .logo{font-size:14px}
.narrow .pay{font-size:9px}
.narrow .foot-base small{margin-left:0}
.mobile .site-footer{padding-top:22px}
.mobile .foot-cols{gap:18px}
</style>
</head>
<body>

<!-- desktop -->
<main class="view desktop">
  <header class="site-header">
    <div class="logo">KELVARO</div>
    <div class="search">Sök skor…</div>
    <nav class="main-nav"><span>DAM</span><span>HERR</span><span>BARN</span><span>REA</span></nav>
    <div class="header-icons">
      <svg class="icon" viewBox="0 0 12 12"><circle cx="6" cy="4" r="2.5" fill="none" stroke="#1b1b1b"/><path d="M1.5 11.5c1-3 8-3 9 0" fill="none" stroke="#1b1b1b"/></svg>
      <svg class="icon" viewBox="0 0 12 12"><path d="M2 4h8l-1 7H3z" fill="none" stroke="#1b1b1b"/><path d="M4 4a2 2 0 0 1 4 0" fill="none" stroke="#1b1b1b"/></svg>
    </div>
  </header>
  <section class="hero" role="img" aria-label="Overhead photo of colourful sneakers arranged in a circle">
    <div class="arrow left"><svg width="6" height="8" viewBox="0 0 6 8"><path d="M5 0 1 4l4 4" stroke="#fff" fill="none"/></svg></div>
    <div class="hero-copy"><div class="off">50% OFF</div><div class="kind">SNEAKERS</div><span class="btn">Shop now</span></div>
    <div class="arrow right"><svg width="6" height="8" viewBox="0 0 6 8"><path d="M1 0l4 4-4 4" stroke="#fff" fill="none"/></svg></div>
  </section>
  <section class="categories">
    <div class="cat" role="img" aria-label="Legs wearing sneakers"><span>SNEAKERS</span></div>
    <div class="cat" role="img" aria-label="Legs wearing boots"><span>BOOTS</span></div>
    <div class="cat" role="img" aria-label="Running shoes in motion"><span>SPORTSKOR</span></div>
    <div class="cat" role="img" aria-label="Sandals on grass"><span>SANDALER</span></div>
  </section>
  <section class="products">
    <div class="product"><div class="shot c1" role="img" aria-label="Shoe photo"></div><b>Arvona</b><span>Lunda Run</span><em>899 kr</em></div>
    <div class="product"><div class="shot c2" role="img" aria-label="Shoe photo"></div><b>Redbay</b><span>Falk Low</span><em>799 kr</em></div>
    <div class="product"><div class="shot c4" role="img" aria-label="Shoe photo"></div><b>Conrade</b><span>Vinga High</span><em>699 kr</em></div>
    <div class="product"><div class="shot c3" role="img" aria-label="Shoe photo"></div><b>Timbrel</b><span>Mossa Boot</span><em>1 499 kr</em></div>
    <div class="product"><div class="shot c1" role="img" aria-label="Shoe photo"></div><b>Skorvo</b><span>Bris Walk</span><em>649 kr</em></div>
    <div class="product"><div class="shot c4" role="img" aria-label="Shoe photo"></div><b>Morvel</b><span>Granit Lace</span><em>1 799 kr</em></div>

    <div class="product"><div class="shot c3" role="img" aria-label="Shoe photo"></div><b>Kinto</b><span>Kusten Sand</span><em>999 kr</em></div>
    <div class="product"><div class="shot c3" role="img" aria-label="Shoe photo"></div><b>Gelvo</b><span>Dimma Low</span><em class="sale">549 kr</em></div>
    <div class="product"><div class="shot c6" role="img" aria-label="Shoe photo"></div><b>Skorvo</b><span>Ljus Step</span><em>599 kr</em></div>
    <div class="product"><div class="shot c4" role="img" aria-label="Shoe photo"></div><b>Conrade</b><span>Rim Strap</span><em class="sale">499 kr</em></div>
    <div class="product"><div class="shot c6" role="img" aria-label="Shoe photo"></div><b>Arvona</b><span>Sol Court</span><em>749 kr</em></div>
    <div class="product"><div class="shot c2" role="img" aria-label="Shoe photo"></div><b>Redbay</b><span>Vik Retro</span><em>849 kr</em></div>

    <div class="product"><div class="shot c5" role="img" aria-label="Shoe photo"></div><b>Kinto</b><span>Myr Trek</span><em>1 099 kr</em></div>
    <div class="product"><div class="shot c4" role="img" aria-label="Shoe photo"></div><b>Timbrel</b><span>Fjäll Hike</span><em>1 399 kr</em></div>
    <div class="product"><div class="shot c4" role="img" aria-label="Shoe photo"></div><b>Morvel</b><span>Sten Ankle</span><em>1 899 kr</em></div>
    <div class="product"><div class="shot c1" role="img" aria-label="Shoe photo"></div><b>Gelvo</b><span>Klippa Air</span><em>1 199 kr</em></div>
    <div class="product"><div class="shot c5" role="img" aria-label="Shoe photo"></div><b>Redbay</b><span>Skog Trail</span><em>999 kr</em></div>
    <div class="product"><div class="shot c2" role="img" aria-label="Shoe photo"></div><b>Arvona</b><span>Moln Pace</span><em>1 599 kr</em></div>

    <div class="product"><div class="shot c1" role="img" aria-label="Shoe photo"></div><b>Arvona</b><span>Norr Speed</span><em>1 699 kr</em></div>
    <div class="product"><div class="shot c2" role="img" aria-label="Shoe photo"></div><b>Redbay</b><span>Frost Train</span><em>1 099 kr</em></div>
    <div class="product"><div class="shot c4" role="img" aria-label="Shoe photo"></div><b>Skorvo</b><span>Tall Comfort</span><em>899 kr</em></div>
    <div class="product"><div class="shot c3" role="img" aria-label="Shoe photo"></div><b>Timbrel</b><span>Hav Deck</span><em>1 199 kr</em></div>
    <div class="product"><div class="shot c3" role="img" aria-label="Shoe photo"></div><b>Gelvo</b><span>Ekdal Slip</span><em class="sale">699 kr</em></div>
    <div class="product"><div class="shot c4" role="img" aria-label="Shoe photo"></div><b>Conrade</b><span>Aska Hi</span><em>1 049 kr</em></div>

    <div class="product"><div class="shot c4" role="img" aria-label="Shoe photo"></div><b>Kinto</b><span>Dal Mid</span><em>1 499 kr</em></div>
    <div class="product"><div class="shot c3" role="img" aria-label="Shoe photo"></div><b>Timbrel</b><span>Björk Boot</span><em>2 199 kr</em></div>
    <div class="product"><div class="shot c4" role="img" aria-label="Shoe photo"></div><b>Morvel</b><span>Kvarts Sole</span><em>2 099 kr</em></div>
    <div class="product"><div class="shot c1" role="img" aria-label="Shoe photo"></div><b>Skorvo</b><span>Glimt Run</span><em>699 kr</em></div>
    <div class="product"><div class="shot c6" role="img" aria-label="Shoe photo"></div><b>Gelvo</b><span>Våg Flow</span><em>1 299 kr</em></div>
    <div class="product"><div class="shot c2" role="img" aria-label="Shoe photo"></div><b>Conrade</b><span>Lind Canvas</span><em>949 kr</em></div>

    <div class="product"><div class="shot c5" role="img" aria-label="Shoe photo"></div><b>Kinto</b><span>Strand Aqua</span><em>1 099 kr</em></div>
    <div class="product"><div class="shot c4" role="img" aria-label="Shoe photo"></div><b>Timbrel</b><span>Tundra Mid</span><em>1 599 kr</em></div>
    <div class="product"><div class="shot c4" role="img" aria-label="Shoe photo"></div><b>Morvel</b><span>Söder Derby</span><em>1 699 kr</em></div>
    <div class="product"><div class="shot c6" role="img" aria-label="Shoe photo"></div><b>Skorvo</b><span>Ängen Lite</span><em class="sale">449 kr</em></div>
    <div class="product"><div class="shot c4" role="img" aria-label="Shoe photo"></div><b>Arvona</b><span>Vind Tempo</span><em>1 249 kr</em></div>
    <div class="product"><div class="shot c2" role="img" aria-label="Shoe photo"></div><b>Redbay</b><span>Ö Classic</span><em>649 kr</em></div>
  </section>
  <span class="more">VISA FLER PRODUKTER</span>
  <section class="usps">
    <div class="usp"><p>Brands for all occasions for<br>children, ladies and gentlemen</p><span class="btn">Read more</span></div>
    <div class="usp"><p>Find the right shoes</p><span class="btn">Read more</span></div>
    <div class="usp"><p>Unique brand online with<br>30 days to open purchase</p><span class="btn">Read more</span></div>
    <div class="usp"><p>Free shipping and<br>return of footwear</p><span class="btn">Read more</span></div>
  </section>
  <section class="promise">
    <p>Always at home in time</p>
    <strong>Always 30 days open purchase!</strong>
    <p>Always Free Shipping and Free Returns!</p>
    <p>Always on payment</p>
  </section>
  <footer class="site-footer">
    <div class="foot-cols">
      <div><h4>Kundservice</h4><p>Kontakt</p><p>Frakt</p><p>Returer</p></div>
      <div><h4>Om oss</h4><p>Företaget</p><p>Jobb</p><p>Press</p></div>
      <div><h4>Villkor</h4><p>Köpvillkor</p><p>Integritet</p><p>Cookies</p></div>
      <div><h4>Följ oss</h4><p>Nyheter</p><p>Blogg</p></div>
      <div><h4>Nyhetsbrev</h4><div class="news"><i></i><b>Skicka</b></div></div>
    </div>
    <div class="foot-base"><div class="logo">KELVARO</div><div class="pay">Vantra</div><small>© Kelvaro 2024</small></div>
  </footer>
</main>

<!-- tablet -->
<main class="view tablet narrow">
  <header class="site-header">
    <svg class="icon" viewBox="0 0 12 12"><path d="M1 3h10M1 6h10M1 9h10" stroke="#1b1b1b"/></svg>
    <div class="logo">KELVARO</div>
    <div class="header-icons">
      <svg class="icon" viewBox="0 0 12 12"><circle cx="5" cy="5" r="3.5" fill="none" stroke="#1b1b1b"/><path d="M8 8l3 3" stroke="#1b1b1b"/></svg>
      <svg class="icon" viewBox="0 0 12 12"><path d="M2 4h8l-1 7H3z" fill="none" stroke="#1b1b1b"/></svg>
    </div>
  </header>
  <section class="hero" role="img" aria-label="Overhead photo of colourful sneakers arranged in a circle">
    <div class="hero-copy"><div class="off">50% OFF</div><div class="kind">SNEAKERS</div><span class="btn">Shop now</span></div>
  </section>
  <section class="categories">
    <div class="cat" role="img" aria-label="Legs wearing sneakers"><span>SNEAKERS</span></div>
    <div class="cat" role="img" aria-label="Legs wearing boots"><span>BOOTS</span></div>
    <div class="cat" role="img" aria-label="Running shoes in motion"><span>SPORTSKOR</span></div>
    <div class="cat" role="img" aria-label="Sandals on grass"><span>SANDALER</span></div>
  </section>
  <section class="products">
    <div class="product"><div class="shot c1" role="img" aria-label="Shoe photo"></div><b>Arvona</b><span>Lunda Run</span><em>899 kr</em></div>
    <div class="product"><div class="shot c2" role="img" aria-label="Shoe photo"></div><b>Redbay</b><span>Falk Low</span><em>799 kr</em></div>
    <div class="product"><div class="shot c4" role="img" aria-label="Shoe photo"></div><b>Conrade</b><span>Vinga High</span><em>699 kr</em></div>
    <div class="product"><div class="shot c3" role="img" aria-label="Shoe photo"></div><b>Timbrel</b><span>Mossa Boot</span><em>1 499 kr</em></div>
    <div class="product"><div class="shot c1" role="img" aria-label="Shoe photo"></div><b>Skorvo</b><span>Bris Walk</span><em>649 kr</em></div>
    <div class="product"><div class="shot c4" role="img" aria-label="Shoe photo"></div><b>Morvel</b><span>Granit Lace</span><em>1 799 kr</em></div>
    <div class="product"><div class="shot c3" role="img" aria-label="Shoe photo"></div><b>Kinto</b><span>Kusten Sand</span><em>999 kr</em></div>
    <div class="product"><div class="shot c3" role="img" aria-label="Shoe photo"></div><b>Gelvo</b><span>Dimma Low</span><em class="sale">549 kr</em></div>
    <div class="product"><div class="shot c6" role="img" aria-label="Shoe photo"></div><b>Skorvo</b><span>Ljus Step</span><em>599 kr</em></div>
    <div class="product"><div class="shot c4" role="img" aria-label="Shoe photo"></div><b>Conrade</b><span>Rim Strap</span><em class="sale">499 kr</em></div>
    <div class="product"><div class="shot c5" role="img" aria-label="Shoe photo"></div><b>Kinto</b><span>Myr Trek</span><em>1 099 kr</em></div>
    <div class="product"><div class="shot c4" role="img" aria-label="Shoe photo"></div><b>Timbrel</b><span>Fjäll Hike</span><em>1 399 kr</em></div>
    <div class="product"><div class="shot c4" role="img" aria-label="Shoe photo"></div><b>Morvel</b><span>Sten Ankle</span><em>1 899 kr</em></div>
    <div class="product"><div class="shot c1" role="img" aria-label="Shoe photo"></div><b>Gelvo</b><span>Klippa Air</span><em>1 199 kr</em></div>
    <div class="product"><div class="shot c3" role="img" aria-label="Shoe photo"></div><b>Timbrel</b><span>Hav Deck</span><em>1 199 kr</em></div>
    <div class="product"><div class="shot c3" role="img" aria-label="Shoe photo"></div><b>Gelvo</b><span>Ekdal Slip</span><em class="sale">699 kr</em></div>
    <div class="product"><div class="shot c6" role="img" aria-label="Shoe photo"></div><b>Skorvo</b><span>Ängen Lite</span><em class="sale">449 kr</em></div>
    <div class="product"><div class="shot c2" role="img" aria-label="Shoe photo"></div><b>Conrade</b><span>Lind Canvas</span><em>949 kr</em></div>
    <div class="product"><div class="shot c1" role="img" aria-label="Shoe photo"></div><b>Arvona</b><span>Vind Tempo</span><em>1 249 kr</em></div>
    <div class="product"><div class="shot c2" role="img" aria-label="Shoe photo"></div><b>Redbay</b><span>Ö Classic</span><em>649 kr</em></div>
  </section>
  <span class="more">VISA FLER</span>
  <section class="usps">
    <div class="usp"><p>Brands for all occasions for children, ladies and gentlemen</p><span class="btn">Read more</span></div>
    <div class="usp"><p>Find the right shoes</p><span class="btn">Read more</span></div>
    <div class="usp"><p>Unique brand online with 30 days to open purchase</p><span class="btn">Read more</span></div>
    <div class="usp"><p>Free shipping and return of footwear</p><span class="btn">Read more</span></div>
  </section>
  <section class="promise">
    <p>Always at home in time</p>
    <strong>Always 30 days open purchase!</strong>
    <p>Always Free Shipping and Free Returns!</p>
  </section>
  <footer class="site-footer">
    <div class="foot-cols">
      <div><h4>Kundservice</h4><p>Kontakt · Frakt · Returer</p></div>
      <div><h4>Nyhetsbrev</h4><div class="news"><i></i><b>Skicka</b></div></div>
    </div>
    <div class="foot-base"><div class="logo">KELVARO</div><div class="pay">Vantra</div></div>
  </footer>
</main>

<!-- mobile -->
<main class="view mobile narrow">
  <header class="site-header">
    <svg class="icon" viewBox="0 0 12 12"><path d="M1 3h10M1 6h10M1 9h10" stroke="#1b1b1b"/></svg>
    <div class="logo">KELVARO</div>
    <div class="header-icons">
      <svg class="icon" viewBox="0 0 12 12"><circle cx="5" cy="5" r="3.5" fill="none" stroke="#1b1b1b"/><path d="M8 8l3 3" stroke="#1b1b1b"/></svg>
      <svg class="icon" viewBox="0 0 12 12"><path d="M2 4h8l-1 7H3z" fill="none" stroke="#1b1b1b"/></svg>
    </div>
  </header>
  <section class="hero" role="img" aria-label="Overhead photo of colourful sneakers arranged in a circle">
    <div class="hero-copy"><div class="off">50% OFF</div><div class="kind">SNEAKERS</div><span class="btn">Shop now</span></div>
  </section>
  <section class="categories">
    <div class="cat" role="img" aria-label="Legs wearing sneakers"><span>SNEAKERS</span></div>
    <div class="cat" role="img" aria-label="Legs wearing boots"><span>BOOTS</span></div>
    <div class="cat" role="img" aria-label="Running shoes in motion"><span>SPORTSKOR</span></div>
    <div class="cat" role="img" aria-label="Sandals on grass"><span>SANDALER</span></div>
  </section>
  <section class="products">
    <div class="product"><div class="shot c1" role="img" aria-label="Shoe photo"></div><b>Arvona</b><span>Lunda Run</span><em>899 kr</em></div>
    <div class="product"><div class="shot c2" role="img" aria-label="Shoe photo"></div><b>Redbay</b><span>Falk Low</span><em>799 kr</em></div>
    <div class="product"><div class="shot c4" role="img" aria-label="Shoe photo"></div><b>Conrade</b><span>Vinga High</span><em>699 kr</em></div>
    <div class="product"><div class="shot c3" role="img" aria-label="Shoe photo"></div><b>Timbrel</b><span>Mossa Boot</span><em>1 499 kr</em></div>
    <div class="product"><div class="shot c1" role="img" aria-label="Shoe photo"></div><b>Skorvo</b><span>Bris Walk</span><em>649 kr</em></div>
    <div class="product"><div class="shot c4" role="img" aria-label="Shoe photo"></div><b>Morvel</b><span>Granit Lace</span><em>1 799 kr</em></div>
    <div class="product"><div class="shot c3" role="img" aria-label="Shoe photo"></div><b>Kinto</b><span>Kusten Sand</span><em>999 kr</em></div>
    <div class="product"><div class="shot c3" role="img" aria-label="Shoe photo"></div><b>Gelvo</b><span>Dimma Low</span><em class="sale">549 kr</em></div>
    <div class="product"><div class="shot c6" role="img" aria-label="Shoe photo"></div><b>Skorvo</b><span>Ljus Step</span><em>599 kr</em></div>
    <div class="product"><div class="shot c4" role="img" aria-label="Shoe photo"></div><b>Conrade</b><span>Rim Strap</span><em class="sale">499 kr</em></div>
    <div class="product"><div class="shot c5" role="img" aria-label="Shoe photo"></div><b>Kinto</b><span>Myr Trek</span><em>1 099 kr</em></div>
    <div class="product"><div class="shot c4" role="img" aria-label="Shoe photo"></div><b>Timbrel</b><span>Fjäll Hike</span><em>1 399 kr</em></div>
    <div class="product"><div class="shot c4" role="img" aria-label="Shoe photo"></div><b>Morvel</b><span>Sten Ankle</span><em>1 899 kr</em></div>
    <div class="product"><div class="shot c1" role="img" aria-label="Shoe photo"></div><b>Gelvo</b><span>Klippa Air</span><em>1 199 kr</em></div>
    <div class="product"><div class="shot c3" role="img" aria-label="Shoe photo"></div><b>Timbrel</b><span>Hav Deck</span><em>1 199 kr</em></div>
    <div class="product"><div class="shot c3" role="img" aria-label="Shoe photo"></div><b>Gelvo</b><span>Ekdal Slip</span><em class="sale">699 kr</em></div>
    <div class="product"><div class="shot c4" role="img" aria-label="Shoe photo"></div><b>Kinto</b><span>Dal Mid</span><em>1 499 kr</em></div>
    <div class="product"><div class="shot c3" role="img" aria-label="Shoe photo"></div><b>Timbrel</b><span>Björk Boot</span><em>2 199 kr</em></div>
    <div class="product"><div class="shot c6" role="img" aria-label="Shoe photo"></div><b>Skorvo</b><span>Ängen Lite</span><em class="sale">449 kr</em></div>
    <div class="product"><div class="shot c2" role="img" aria-label="Shoe photo"></div><b>Conrade</b><span>Lind Canvas</span><em>949 kr</em></div>
    <div class="product"><div class="shot c5" role="img" aria-label="Shoe photo"></div><b>Kinto</b><span>Strand Aqua</span><em>1 099 kr</em></div>
    <div class="product"><div class="shot c4" role="img" aria-label="Shoe photo"></div><b>Morvel</b><span>Söder Derby</span><em>1 699 kr</em></div>
    <div class="product"><div class="shot c1" role="img" aria-label="Shoe photo"></div><b>Arvona</b><span>Vind Tempo</span><em>1 249 kr</em></div>
    <div class="product"><div class="shot c2" role="img" aria-label="Shoe photo"></div><b>Redbay</b><span>Ö Classic</span><em>649 kr</em></div>
  </section>
  <span class="more">VISA FLER</span>
  <section class="usps">
    <div class="usp"><p>Brands for all occasions for children, ladies and gentlemen</p><span class="btn">Read more</span></div>
    <div class="usp"><p>Find the right shoes</p><span class="btn">Read more</span></div>
    <div class="usp"><p>Unique brand online with 30 days to open purchase</p><span class="btn">Read more</span></div>
    <div class="usp"><p>Free shipping and return of footwear</p><span class="btn">Read more</span></div>
  </section>
  <section class="promise">
    <p>Always at home in time</p>
    <strong>Always 30 days open purchase!</strong>
    <p>Always Free Shipping and Free Returns!</p>
  </section>
  <footer class="site-footer">
    <div class="foot-cols">
      <div><h4>Kundservice</h4><p>Kontakt</p><p>Frakt</p><p>Returer</p></div>
      <div><h4>Om oss</h4><p>Företaget</p><p>Jobb</p></div>
      <div><h4>Villkor</h4><p>Köpvillkor</p><p>Integritet</p></div>
      <div><h4>Nyhetsbrev</h4><div class="news"><i></i><b>Skicka</b></div></div>
    </div>
    <div class="foot-base"><div class="logo">KELVARO</div><div class="pay">Vantra</div><small>© Kelvaro 2024</small></div>
  </footer>
</main>

</body>
</html>
```